quarry productions business cards design

design a clean look but creative business card for a production company, I'm a freelance producer and launching my startup, would like to keep a clean professional look but still creative

Target Market(s)

businesses

Industry/Entity Type

video production

Contact Information for Business Card

logo, name (Karl Benn), Title (Producer), (MFA Filmmaking, QTSA Los Angeles), contact number & email ID

Colors

Designer to choose only greyscale colors for use in the design.

Requirements
Must have
• logo, black and white colors, you can play with their shades
Nice to have
• a unique design, not necessarily a typical size card
Should not have
• too colorful or playful

```html
<!DOCTYPE html>
<html lang="en">
<head>
<meta charset="UTF-8">
<title>Quarry Productions — Business Cards</title>
<link rel="stylesheet" href="https://fonts.googleapis.com/css2?family=Inter:wght@400;500;700;800&display=swap">
<style>
  :root {
    --backdrop: #9a9a9a;
    --ink: #000000;
    --paper: #ffffff;
  }
  * { margin: 0; padding: 0; box-sizing: border-box; }
  html, body {
    width: 1200px;
    height: 1200px;
    overflow: hidden;
    background: var(--backdrop);
    font-family: "Inter", sans-serif;
  }
  .card {
    position: absolute;
    left: 262px;
    width: 686px;
    height: 392px;
    overflow: hidden;
  }
  .card--front { top: 165px; background: var(--paper); display: flex; }
  .card--back { top: 653px; background: var(--ink); display: flex; align-items: center; justify-content: center; }

  .details {
    width: 272px;
    height: 100%;
    background: var(--ink);
    color: var(--paper);
    padding: 97px 0 0 40px;
  }
  .details__name { font-size: 23px; font-weight: 500; letter-spacing: 0.3px; line-height: 1.1; }
  .details__title { font-size: 16px; font-weight: 400; line-height: 1.3; margin-top: 1px; }
  .details__company { font-size: 16px; font-weight: 700; margin-top: 22px; line-height: 1.25; }
  .details__line { font-size: 16px; font-weight: 400; line-height: 1.25; letter-spacing: 0.2px; }
  .contact { list-style: none; margin-top: 12px; }
  .contact__item { display: flex; align-items: center; gap: 7px; font-size: 16px; line-height: 1.22; letter-spacing: 0.2px; }
  .contact__icon { width: 12px; height: 12px; fill: var(--paper); flex: none; }

  .brand-panel {
    flex: 1;
    display: flex;
    align-items: center;
    justify-content: center;
    padding-bottom: 24px;
  }
  .wordmark {
    font-weight: 800;
    text-transform: uppercase;
    line-height: 0.95;
    letter-spacing: 0.5px;
  }
  .wordmark--front { color: var(--ink); font-size: 40px; text-align: center; }
  .wordmark--back { color: var(--paper); font-size: 38px; }
  .wordmark small { display: block; font-size: 0.62em; font-weight: 800; margin-top: 4px; }
  .back-lockup { display: flex; align-items: center; gap: 22px; margin-top: -12px; }
  .back-lockup__square { width: 58px; height: 58px; background: var(--paper); }
</style>
</head>
<body>

<section class="card card--front" aria-label="Business card front">
  <div class="details">
    <p class="details__name">KARL BENN</p>
    <p class="details__title">Producer</p>
    <p class="details__company">Quarry Productions</p>
    <p class="details__line">MFA Filmmaking</p>
    <p class="details__line">QTSA Los Angeles</p>
    <ul class="contact">
      <li class="contact__item">
        <svg class="contact__icon" viewBox="0 0 24 24" aria-hidden="true"><path d="M6.6 10.8a15.1 15.1 0 0 0 6.6 6.6l2.2-2.2a1 1 0 0 1 1-.25 11.4 11.4 0 0 0 3.6.57 1 1 0 0 1 1 1V20a1 1 0 0 1-1 1A17 17 0 0 1 3 4a1 1 0 0 1 1-1h3.5a1 1 0 0 1 1 1c0 1.25.2 2.45.57 3.57a1 1 0 0 1-.25 1z"/></svg>
        418-302-7746
      </li>
      <li class="contact__item">
        <svg class="contact__icon" viewBox="0 0 24 24" aria-hidden="true"><path d="M2 5h20v14H2z M3.5 6.5 12 13l8.5-6.5" fill="none" stroke="#fff" stroke-width="0"/><path d="M2 5h20v2l-10 6.5L2 7z"/><path d="M2 9l10 6.5L22 9v10H2z"/></svg>
        info@quarryprod.com
      </li>
      <li class="contact__item">
        <svg class="contact__icon" viewBox="0 0 24 24" aria-hidden="true"><circle cx="12" cy="12" r="10"/><path d="M7 6c2 1 1 3 3 4s1 3 3 3 1 3 0 5M15 4c-1 2 1 3 3 3s2 2 3 2" stroke="#000" stroke-width="2" fill="none"/></svg>
        www.quarryprod.com
      </li>
    </ul>
  </div>
  <div class="brand-panel">
    <p class="wordmark wordmark--front">Quarry<small>Productions</small></p>
  </div>
</section>

<section class="card card--back" aria-label="Business card back">
  <div class="back-lockup">
    <span class="back-lockup__square" aria-hidden="true"></span>
    <p class="wordmark wordmark--back">Quarry<small>Productions</small></p>
  </div>
</section>

</body>
</html>
```